Tamarack Hearth Partners Business Card

Looking for a new business card layout. We are a real estate firm w/ a logo, old design attached. Must keep the same elements on there, just need a fresh look and possible some foil accents. Looking for a simpler design w/ more modern style.

Target Market(s)

Real Estate clients

Industry/Entity Type

Real Estate Agent

Contact Information for Business Card

see attached

Font styles to use
Sans Serif

Requirements
Must have
• all elements on current biz card
Nice to have
• modern look, simpler than we have!
Should not have
• no serif fonts

```html
<!DOCTYPE html>
<html lang="en">
<head>
<meta charset="utf-8">
<title>Tamarack Hearth Partners – Business Card</title>
<link href="https://fonts.googleapis.com/css2?family=Montserrat:wght@400;500;600;800&display=swap" rel="stylesheet">
<style>
  :root {
    --backdrop: #d9d9d9;
    --card-gray: #4a4a4c;
    --card-gray-light: #5e5e60;
    --lime: #a6d23a;
    --lime-light: #b5dc4e;
    --ink: #1d1d1d;
    --white: #ffffff;
    --photo-warm: #c9b89a;
    --photo-cool: #8fb5b0;
  }
  * { box-sizing: border-box; margin: 0; padding: 0; }
  html, body {
    width: 1200px; height: 900px; overflow: hidden;
    background: var(--backdrop);
    font-family: "Montserrat", sans-serif;
  }
  .canvas {
    width: 1200px; height: 900px;
    display: flex; flex-direction: column; align-items: center; justify-content: center;
    gap: 36px;
  }
  .card {
    width: 700px; height: 400px;
    border-radius: 26px;
    position: relative; overflow: hidden;
    box-shadow: 0 10px 24px rgba(0,0,0,.22);
  }

  /* Back */
  .card-back {
    background: radial-gradient(ellipse at 45% 35%, var(--card-gray-light), var(--card-gray) 70%);
    display: flex; align-items: center; justify-content: center;
  }
  .wordmark {
    font-weight: 800; color: var(--lime);
    text-transform: uppercase; line-height: 1.05; letter-spacing: 1px;
  }
  .card-back .wordmark { font-size: 44px; text-align: center; }

  /* Front */
  .card-front { background: var(--card-gray); }
  .portrait {
    position: absolute; left: 0; top: 0;
    width: 320px; height: 372px;
    border-bottom-right-radius: 26px;
    background: linear-gradient(160deg, #ece8e2 0%, var(--photo-warm) 45%, var(--photo-cool) 100%);
  }
  .brand-panel {
    position: absolute; left: 320px; top: 0; right: 0; height: 196px;
    background: linear-gradient(135deg, var(--lime-light), var(--lime));
    border-left: 3px solid var(--ink);
    padding: 26px 30px 0 34px;
    text-align: right;
  }
  .brand-panel .wordmark { color: var(--ink); font-size: 27px; text-align: left; }
  .agent-name { margin-top: 14px; font-size: 22px; font-weight: 600; color: var(--ink); }
  .agent-title { font-size: 17px; font-weight: 400; color: #39420f; }
  .address {
    position: absolute; right: 30px; top: 206px;
    display: none;
  }
  .details {
    position: absolute; right: 30px; top: 212px;
    text-align: right; color: var(--white);
    font-size: 17px; line-height: 1.62;
  }
  .details .postal { color: var(--lime); font-size: 15px; line-height: 1.4; margin-bottom: 10px; }
  .contact-line { display: flex; align-items: center; justify-content: flex-end; gap: 10px; }
  .contact-line svg { width: 22px; height: 22px; flex: none; }
  .contact-line.no-icon { padding-right: 32px; }
</style>
</head>
<body>
<main class="canvas">

  <section class="card card-back" aria-label="Card back">
    <div class="wordmark">Tamarack Hearth<br>Partners</div>
  </section>

  <section class="card card-front" aria-label="Card front">
    <div class="portrait" role="img" aria-label="Portrait photo of the broker"></div>

    <div class="brand-panel">
      <div class="wordmark">Tamarack Hearth Partners</div>
      <div class="agent-name">Dana Whitlock</div>
      <div class="agent-title">Principal Broker</div>
    </div>

    <div class="details">
      <div class="postal">482 NW Juniper Ave.<br>Pine Hollow, OR 97000</div>
      <div class="contact-line">+555.210.4418
        <svg viewBox="0 0 24 24" aria-hidden="true"><circle cx="12" cy="12" r="10.5" fill="none" stroke="#a6d23a" stroke-width="1.6"/><rect x="7" y="10" width="10" height="7" rx="1.5" fill="#a6d23a"/><path d="M6.5 10 Q12 5 17.5 10" fill="none" stroke="#a6d23a" stroke-width="1.8"/></svg>
      </div>
      <div class="contact-line">+555.317.9062
        <svg viewBox="0 0 24 24" aria-hidden="true"><circle cx="12" cy="12" r="10.5" fill="none" stroke="#a6d23a" stroke-width="1.6"/><rect x="9" y="6" width="6" height="12" rx="1.2" fill="none" stroke="#a6d23a" stroke-width="1.6"/><circle cx="12" cy="15.8" r=".9" fill="#a6d23a"/></svg>
      </div>
      <div class="contact-line">dana@tamarackhearth.com
        <svg viewBox="0 0 24 24" aria-hidden="true"><circle cx="12" cy="12" r="10.5" fill="none" stroke="#a6d23a" stroke-width="1.6"/><rect x="6.5" y="8" width="11" height="8" rx="1" fill="#a6d23a"/><path d="M6.5 8.5 L12 12.5 L17.5 8.5" fill="none" stroke="#4a4a4c" stroke-width="1.2"/></svg>
      </div>
      <div class="contact-line">tamarackhearth-realty.com
        <svg viewBox="0 0 24 24" aria-hidden="true"><circle cx="12" cy="12" r="10.5" fill="none" stroke="#a6d23a" stroke-width="1.6"/><circle cx="12" cy="12" r="6" fill="none" stroke="#a6d23a" stroke-width="1.3"/><ellipse cx="12" cy="12" rx="2.6" ry="6" fill="none" stroke="#a6d23a" stroke-width="1.1"/><path d="M6 12 H18" stroke="#a6d23a" stroke-width="1.1"/></svg>
      </div>
    </div>
  </section>

</main>
</body>
</html>
```